Logo and Website Design for KR.DN Horizont - a Software Engineering and IT company

Software engineering and IT are two different disciplines - and yet inseparably linked. At KR.DN Horizont, we combine both worlds and ensure that our software solutions are not only innovative and powerful, but also integrate perfectly into existing IT landscapes. Vision stands more for imagination, so it is not neccessary something what has to do with visualisation. Please consider that the winning competitor is also instructed to make a logo for the company. So please make a suitable logo for KR.DN Horizont to which the website fits to and show it during the website creation process. A good Logo desing is important for winning the competition. The website should contain a landing page with inspiring, perhaps futuristic photos of a datacenter and lines of code. Eventuelly flewent integrated in the text. On the landing page the company should introduced with a small text (max 250 words) followed by a section with a short text to one of our products nearby a graphic visualising the architecture of the product. The menue should be on top and fixed during scrolling and consist of the menue items home, solutions, who are we and a contact button. There should be a footer for linking social media, rights and Impressum. Only as an idea not a must. The very first view on the landing page could also be the menue bar and below of it a transparent unsharp photo (e.g. datacenter, lines of code, both ;) with the company name in the center.

###############################################################

Hi Designers,

Despite your very good approaches for describing KR.DN Horizont, here a short introduction (german text) from ourself:

------
KR.DN Horizont – Ihr Partner für ganzheitliche Softwarelösungen

Die KR.DN Horizont ist ein dynamisches Unternehmen, das sich nicht nur auf die Konzeption, das Design und die Entwicklung maßgeschneiderter Software spezialisiert hat, sondern auch deren reibungslosen Betrieb sicherstellt. Mit einem Team aus erfahrenen Softwarearchitekten und IT-Professionals verbinden wir modernste Softwareentwicklung mit tiefgehendem IT-Know-how – für Lösungen, die nachhaltig, leistungsstark und zukunftssicher sind.

Software Engineering trifft IT – Perfektion in Kombination
Software Engineering und IT sind zwei unterschiedliche Disziplinen – und doch untrennbar miteinander verbunden. Wir bei KR.DN Horizont vereinen beide Welten und sorgen dafür, dass unsere Softwarelösungen nicht nur innovativ und leistungsfähig sind, sondern sich auch perfekt in bestehende IT-Landschaften integrieren.

Expertise mit Fokus auf Healthcare & komplexe IT-Umgebungen
Unsere Experten bringen jahrzehntelange Erfahrung aus dem Healthcare-Sektor mit und unterstützen IT-Abteilungen großer Kliniken in der Entwicklung und Optimierung von Softwarelösungen. Von Anwendungssoftware bis hin zu Steuerungssystemen – unsere Softwareingenieure wissen genau, worauf es ankommt.

Ganzheitlicher Ansatz – über die Software hinaus
Wir entwickeln nicht nur Software, sondern übernehmen auch die Verantwortung für deren stabile und effiziente Betriebsumgebung. Egal, ob on-premises, in der Cloud oder als SaaS-Lösung – wir kümmern uns um den kompletten Lifecycle Ihrer Anwendung.

Ihre Vision – unsere Mission.
Ob Neuentwicklung einer SaaS-Anwendung oder die Migration bestehender Lösungen in eine moderne SaaS-Umgebung – mit KR.DN Horizont haben Sie einen starken Partner an Ihrer Seite.

Lassen Sie uns gemeinsam die Zukunft Ihrer Software gestalten!
--------------

Our first solution called "Clear Record Transfer Gateway" (CLARG)
-------------------
Teilen Sie Ihre Daten sicher – ohne Kompromisse!

Sie nutzen eine relationale Datenbank (Veltrix, Bravo Store, Quillbase etc.) und möchten ausgewählte Daten mit Dritten teilen – sei es für ein Data Warehouse, Business Controller, Lieferanten oder Kunden? Doch dabei sollen Datensicherheit, Integrität und Verfügbarkeit Ihrer primären Lösung in keiner Weise gefährdet werden?

Mit unserer Lösung erhalten Sie genau das: Maximalen Schutz für Ihre Anwendung bei gleichzeitigem Nutzen durch autorisierte Dritte – ganz ohne teure Lizenzkosten für eine Schattendatenbank.

Lassen Sie uns gemeinsam herausfinden, wie Sie Ihre Daten sicher und effizient nutzen können. Kontaktieren Sie uns – wir zeigen Ihnen, was möglich ist!
---------------------

Our second solution PLUM:
---------------------
PLUM – Program for a Tone Verification Instrument ist die smarte Lösung für Unternehmen, die bei Farbgenauigkeit keine Kompromisse machen. Die Software erkennt Farbabweichungen zwischen Mustern vollautomatisch, beschreibt sie verständlich und sorgt so für gleichbleibend hohe Produktqualität – schnell, visuell und präzise. Perfekt für alle, die Farbe zur Vertrauenssache machen.
-------------------------

Thanks,
Matthias

Target Market(s)

IT Professionals from any sector

Industry/Entity Type

Healthcare and other

Coding

Coded - Design and coding required

Number of Pages Required

1 page

Font styles to use
Sans Serif

Colors
0054AA
0677BA
7BADD7
CADEEF
E8F1F8
0094D4
00A9DD
6FCCEA
C7EBF8
E9F6FB
00AB8E
00BBA5
67D7C9
C6EFE9
E9F9F6

Requirements
Must have
• Please see description
Nice to have
• On the landing page the company should introduced with a small text (max 250 words) followed by a section with a short text to one of our products nearby a graphic visualising the architecture of the product. The menue should be on top and fixed during scrolling and consist of the menue items home, solutions, who are we and a contact button. There should be a footer for linking social media, rights and Impressum. Only as an idea not a must. The very first view on the landing page could also be the menue bar and below of it a transparent unsharp photo (e.g. datacenter, lines of code, both ;) with the company name in the center.
Should not have
• Please see description

```html
<!DOCTYPE html>
<html lang="en">
<head>
<meta charset="utf-8">
<title>KR.DN Horizont – Hero Slides</title>
<link rel="stylesheet" href="https://fonts.googleapis.com/css2?family=Lato:wght@400;700;900&display=swap">
<style>
  :root {
    --accent: #1ba3d6;
    --accent-deep: #0094d4;
    --white: #ffffff;
    --page: #ffffff;
    --navy-1: #0a1a3a;
    --navy-2: #0d3d6e;
    --teal-1: #0c4a6a;
    --indigo-1: #0b1550;
    --indigo-2: #1b3a8a;
  }
  * { box-sizing: border-box; margin: 0; padding: 0; }
  html, body {
    width: 719px; height: 1200px; overflow: hidden;
    background: var(--page);
    font-family: "Lato", sans-serif;
  }
  .hero {
    position: absolute; left: 43px; width: 609px; height: 345px;
    color: var(--white);
  }
  .hero--datacenter { top: 34px; }
  .hero--code { top: 426px; }
  .hero--connect { top: 817px; }
  .hero__backdrop { position: absolute; inset: 0; width: 609px; height: 345px; }
  .brand {
    position: absolute; left: 57px; top: 16px; height: 28px;
    display: flex; align-items: center; gap: 7px;
  }
  .brand__dot {
    width: 26px; height: 26px; border-radius: 50%;
    border: 2.5px solid var(--white);
  }
  .brand__name {
    font-weight: 700; font-size: 16px; letter-spacing: 0.2px;
    text-transform: uppercase; white-space: nowrap;
  }
  .nav__item {
    position: absolute; top: 21px; height: 17px; line-height: 17px;
    font-size: 8px; padding: 0 7px; border-radius: 1px; white-space: nowrap;
  }
  .nav__item--active { background: var(--accent); }
  .nav__home { left: 260px; }
  .nav__solutions { left: 305px; }
  .nav__who { left: 361px; }
  .nav__contact { left: 430px; }
  .btn {
    position: absolute; background: var(--accent); color: var(--white);
    font-weight: 700; text-align: center; border-radius: 1px; white-space: nowrap;
  }
  .btn--header { left: 482px; top: 19px; width: 70px; height: 22px; line-height: 22px; font-size: 8px; }
  .hero__title {
    position: absolute; left: 0; right: 0; text-align: center;
    font-weight: 700; font-size: 40px; line-height: 40px;
    text-transform: uppercase; letter-spacing: -0.3px;
  }
  .hero__lead {
    position: absolute; left: 0; right: 0; text-align: center;
    font-size: 11px; line-height: 16px;
  }
  .btn--cta {
    height: 22px; line-height: 22px; font-size: 8px;
    left: 50%; transform: translateX(-50%); padding: 0 16px;
  }
  .dots {
    position: absolute; top: 301px; left: 0; right: 0;
    display: flex; justify-content: center; gap: 4px;
  }
  .dots span { width: 6px; height: 6px; border-radius: 50%; background: rgba(255,255,255,.55); }
  .dots span.is-active { background: var(--white); }
</style>
</head>
<body>

<!-- Slide 1 -->
<section class="hero hero--datacenter">
  <svg class="hero__backdrop" viewBox="0 0 609 345" role="img" aria-label="Photo of a glowing blue data centre aisle lined with server racks">
    <defs>
      <radialGradient id="bgDatacenter" cx="50%" cy="45%" r="70%">
        <stop offset="0" stop-color="#1f6fa8"/>
        <stop offset="0.5" stop-color="#0d3d6e"/>
        <stop offset="1" stop-color="#071630"/>
      </radialGradient>
    </defs>
    <path d="M0 0 H609 V283 Q304.5 377 0 283 Z" fill="url(#bgDatacenter)"/>
    <path d="M0 283 Q304.5 377 609 283 L571 297 Q304.5 381 38 297 Z" fill="#1ba3d6"/>
  </svg>
  <div class="brand"><span class="brand__dot"></span><span class="brand__name">KR.DN Horizont</span></div>
  <span class="nav__item nav__home">Home</span>
  <span class="nav__item nav__solutions">Solutions</span>
  <span class="nav__item nav__who nav__item--active">Who Are We</span>
  <span class="nav__item nav__contact">Contact</span>
  <span class="btn btn--header">Get Started</span>
  <h1 class="hero__title" style="top:130px">Code with Purpose</h1>
  <p class="hero__lead" style="top:182px">Future-forward solutions—designed for innovation, built to integrate<br>seamlessly into today’s complex IT landscapes.</p>
  <span class="btn btn--cta" style="top:226px">Meet the Team</span>
  <div class="dots"><span class="is-active"></span><span></span><span></span><span></span></div>
</section>

<!-- Slide 2 -->
<section class="hero hero--code">
  <svg class="hero__backdrop" viewBox="0 0 609 345" role="img" aria-label="Blurred photo of lines of code floating in teal light">
    <defs>
      <radialGradient id="bgCode" cx="50%" cy="40%" r="70%">
        <stop offset="0" stop-color="#176a82"/>
        <stop offset="0.55" stop-color="#0c3a66"/>
        <stop offset="1" stop-color="#060c38"/>
      </radialGradient>
    </defs>
    <path d="M0 0 H609 V283 Q304.5 377 0 283 Z" fill="url(#bgCode)"/>
    <path d="M0 283 Q304.5 377 609 283 L571 297 Q304.5 381 38 297 Z" fill="#1ba3d6"/>
  </svg>
  <div class="brand"><span class="brand__dot"></span><span class="brand__name">KR.DN Horizont</span></div>
  <span class="nav__item nav__home">Home</span>
  <span class="nav__item nav__solutions nav__item--active">Solutions</span>
  <span class="nav__item nav__who">Who Are We</span>
  <span class="nav__item nav__contact">Contact</span>
  <span class="btn btn--header">Get Started</span>
  <h1 class="hero__title" style="top:124px">Engineered to Integrate</h1>
  <p class="hero__lead" style="top:173px">Our software solutions plug into your existing IT like they were meant to<br>be there—from day one.</p>
  <span class="btn btn--cta" style="top:217px">View Our Work</span>
  <div class="dots"><span class="is-active"></span><span></span><span></span><span></span></div>
</section>

<!-- Slide 3 -->
<section class="hero hero--connect">
  <svg class="hero__backdrop" viewBox="0 0 609 345" role="img" aria-label="Photo of a server room corridor with a glowing cloud outline">
    <defs>
      <radialGradient id="bgConnect" cx="50%" cy="45%" r="70%">
        <stop offset="0" stop-color="#2a4fa6"/>
        <stop offset="0.55" stop-color="#172f78"/>
        <stop offset="1" stop-color="#0a1240"/>
      </radialGradient>
    </defs>
    <path d="M0 0 H609 V283 Q304.5 377 0 283 Z" fill="url(#bgConnect)"/>
    <path d="M0 283 Q304.5 377 609 283 L571 297 Q304.5 381 38 297 Z" fill="#1ba3d6"/>
  </svg>
  <div class="brand"><span class="brand__dot"></span><span class="brand__name">KR.DN Horizont</span></div>
  <span class="nav__item nav__home">Home</span>
  <span class="nav__item nav__solutions">Solutions</span>
  <span class="nav__item nav__who">Who Are We</span>
  <span class="nav__item nav__contact nav__item--active">Contact</span>
  <span class="btn btn--header">Get Started</span>
  <h1 class="hero__title" style="top:130px">Ready to Connect?</h1>
  <p class="hero__lead" style="top:183px">Let’s talk about your goals and how we can bring them to<br>life—one solution at a time.</p>
  <span class="btn btn--cta" style="top:226px">Start the Conversation</span>
  <div class="dots"><span class="is-active"></span><span></span><span></span><span></span></div>
</section>

</body>
</html>
```